Flyer design for the Harvest Of Light Summit 2019 (HOLVIRE)

Design a flyer for our annual conference with basic information about the conference: conference logo and year, Conference name: Harvest Of Light Summit Location: Tallow Community Center (Downtown Portland)382 Wimbrel Lane, Portland, ME 04107, Date: August 8th, 9th, 10th and 11th, 2019Start time 7:00PMI would like the following three words added to the flyer. These words describe the vision of the conference: Prophetic, Fire, Overflow,

Contact info:
Website: www.quentavo.org
Phone: 207 555 0143
Email: contact@plumvesta.org

Target Market(s)

Young adults living in the United States

Industry/Entity Type

Religious

Font styles to use
Sans Serif

Colors

Designer to choose colors to be used in the design.

Requirements
Must have
• HOLVIRE must logo standout, the reader should be able to take a quick look and find key info,
Should not have
• Cross image, church image

```html
<!DOCTYPE html>
<html lang="en">
<head>
<meta charset="utf-8">
<title>Harvest Of Light Summit 2019 – Flyer</title>
<link href="https://fonts.googleapis.com/css2?family=Montserrat:wght@400;600;700;800;900&family=Oswald:wght@300;400&display=swap" rel="stylesheet">
<style>
  :root{
    --board:#666666;
    --orange:#f39321;
    --blue:#1f73b7;
    --blue-soft:#2f7fbd;
    --white:#ffffff;
    --ink:#1e1e1e;
    --bar-dark:#2b2b2b;
    --caption:#eeeeee;
  }
  *{margin:0;padding:0;box-sizing:border-box}
  html,body{width:1200px;height:859px;overflow:hidden;background:var(--board)}
  body{position:relative;font-family:"Montserrat",sans-serif}

  .flyer{position:absolute;top:44px;width:500px;height:706px;overflow:hidden;
    box-shadow:0 14px 22px rgba(0,0,0,.35)}
  .flyer--gradient{left:72px}
  .flyer--orange{left:621px;width:504px}

  .masthead{position:absolute;left:0;top:0;width:100%;height:116px;background:var(--white)}
  .brand{position:absolute;top:18px;width:100%;text-align:center;
    font-weight:800;font-size:56px;line-height:1;color:var(--blue);letter-spacing:1px}
  .brand-year{position:absolute;top:78px;left:0;width:100%;display:flex;justify-content:center;align-items:center;gap:12px}
  .brand-year .rule{width:72px;height:2px;background:var(--orange)}
  .brand-year span{font-weight:700;font-size:30px;line-height:1;color:var(--orange);letter-spacing:15px;margin-right:-15px}

  .body{position:absolute;left:0;top:116px;width:100%;height:534px}
  .flyer--gradient .body{background:linear-gradient(180deg,var(--orange) 0%,#c08a3c 30%,#7a8c86 60%,var(--blue-soft) 85%,var(--blue) 100%)}
  .flyer--orange .body{height:540px;background:var(--orange)}

  .kicker{position:absolute;top:26px;width:100%;text-align:center;font-weight:800;font-size:42px;
    color:var(--white);letter-spacing:1px;line-height:1}
  .headline{position:absolute;top:68px;width:100%;text-align:center;font-weight:900;font-size:122px;
    color:var(--white);line-height:1;letter-spacing:-2px}

  .pillars{position:absolute;top:210px;left:60px;width:380px;height:46px;display:flex;justify-content:center;align-items:center;
    font-family:"Oswald",sans-serif;font-weight:400;font-size:33px;color:var(--white);gap:10px}
  .pillars .sep{width:2px;height:30px;background:var(--orange)}
  .flyer--orange .pillars{background:var(--ink)}

  .venue{position:absolute;top:276px;width:100%;text-align:center;color:var(--white)}
  .venue-label{font-size:13px;font-weight:400;margin-bottom:4px}
  .venue-address{font-size:16.5px;font-weight:700;line-height:22px}
  .flyer--orange .venue-label{color:var(--ink)}

  .dates{position:absolute;top:388px;left:66px;width:368px;height:122px;border:1px solid var(--white);border-radius:10px;
    text-align:center;color:var(--white);padding:0;margin:0;min-inline-size:0}
  .dates-label{margin:0 auto;padding:0 9px;font-size:14px;line-height:18px;white-space:nowrap}
  .dates-range{margin-top:4px;font-weight:800;font-size:33px;line-height:36px}
  .dates-year{font-weight:800;font-size:33px;line-height:36px}
  .dates-time{margin-top:3px;font-size:16px;line-height:24px}
  .dates-time b{font-weight:800;font-size:21px}
  .flyer--orange .dates-range,.flyer--orange .dates-year{color:var(--ink)}

  .contact{position:absolute;left:0;bottom:0;width:100%;height:56px;display:flex;justify-content:center;align-items:center;gap:16px;
    font-size:10.5px;font-weight:600;text-transform:uppercase}
  .flyer--gradient .contact{background:var(--bar-dark);color:var(--white)}
  .flyer--orange .contact{height:51px;background:var(--white);color:var(--ink)}
  .contact-item{display:flex;align-items:center;gap:6px}
  .contact-item svg{width:16px;height:16px}

  .board-label{position:absolute;top:768px;font-size:22px;color:var(--caption)}
  .board-label--left{left:70px}
  .board-label--right{right:82px}
  .board-caption{position:absolute;top:803px;width:100%;text-align:center;font-size:22px;color:var(--caption)}
</style>
</head>
<body>

<svg width="0" height="0" style="position:absolute" aria-hidden="true">
  <defs>
    <symbol id="icon-web" viewBox="0 0 16 16"><circle cx="8" cy="8" r="8" fill="#f39321"/><circle cx="8" cy="8" r="4.2" fill="none" stroke="#fff" stroke-width="1"/><path d="M3.8 8h8.4M8 3.8c-2 2.5-2 5.9 0 8.4M8 3.8c2 2.5 2 5.9 0 8.4" fill="none" stroke="#fff" stroke-width="1"/></symbol>
    <symbol id="icon-phone" viewBox="0 0 16 16"><circle cx="8" cy="8" r="8" fill="#f39321"/><path d="M6 4.2l1.3 2.2-1 .9c.5 1.1 1.3 2 2.3 2.5l.9-1 2.2 1.3-.7 1.5c-3.3-.3-6.1-3.2-6.4-6.5z" fill="#fff"/></symbol>
    <symbol id="icon-mail" viewBox="0 0 16 16"><circle cx="8" cy="8" r="8" fill="#f39321"/><rect x="4.2" y="5.2" width="7.6" height="5.6" rx=".6" fill="#fff"/><path d="M4.5 5.6L8 8.3l3.5-2.7" fill="none" stroke="#f39321" stroke-width="1"/></symbol>
  </defs>
</svg>

<article class="flyer flyer--gradient">
  <header class="masthead">
    <div class="brand">HOLVIRE</div>
    <div class="brand-year"><i class="rule"></i><span>2019</span><i class="rule"></i></div>
  </header>
  <section class="body">
    <div class="kicker">HARVEST OF</div>
    <div class="headline">LIGHT</div>
    <div class="pillars">PROPHETIC<i class="sep"></i>FIRE<i class="sep"></i>OVERFLOW</div>
    <div class="venue">
      <p class="venue-label">Conference Location at</p>
      <p class="venue-address">Tallow Community Center<br>(Downtown Portland) 382 Wimbrel Lane,<br>Portland, ME 04107</p>
    </div>
    <fieldset class="dates">
      <legend class="dates-label">Conference Date on</legend>
      <p class="dates-range">AUGUST 8TH - 11TH</p>
      <p class="dates-year">2019</p>
      <p class="dates-time">Start time <b>7:00PM</b></p>
    </fieldset>
  </section>
  <footer class="contact">
    <span class="contact-item"><svg><use href="#icon-web"/></svg>www.quentavo.org</span>
    <span class="contact-item"><svg><use href="#icon-phone"/></svg>207 555 0143</span>
    <span class="contact-item"><svg><use href="#icon-mail"/></svg>contact@plumvesta.org</span>
  </footer>
</article>

<article class="flyer flyer--orange">
  <header class="masthead">
    <div class="brand">HOLVIRE</div>
    <div class="brand-year"><i class="rule"></i><span>2019</span><i class="rule"></i></div>
  </header>
  <section class="body">
    <div class="kicker">HARVEST OF</div>
    <div class="headline">LIGHT</div>
    <div class="pillars">PROPHETIC<i class="sep"></i>FIRE<i class="sep"></i>OVERFLOW</div>
    <div class="venue">
      <p class="venue-label">Conference Location at</p>
      <p class="venue-address">Tallow Community Center<br>(Downtown Portland) 382 Wimbrel Lane,<br>Portland, ME 04107</p>
    </div>
    <fieldset class="dates">
      <legend class="dates-label">Conference Date on</legend>
      <p class="dates-range">AUGUST 8TH - 11TH</p>
      <p class="dates-year">2019</p>
      <p class="dates-time">Start time <b>7:00PM</b></p>
    </fieldset>
  </section>
  <footer class="contact">
    <span class="contact-item"><svg><use href="#icon-web"/></svg>www.quentavo.org</span>
    <span class="contact-item"><svg><use href="#icon-phone"/></svg>207 555 0143</span>
    <span class="contact-item"><svg><use href="#icon-mail"/></svg>contact@plumvesta.org</span>
  </footer>
</article>

<p class="board-label board-label--left">Sample3</p>
<p class="board-label board-label--right">Sample4</p>
<p class="board-caption">Harvest Of Light Summit 2019</p>

</body>
</html>
```